Website for new dental office

I am Dr. Colin Marsh and am building a new dental practice. I specialize in general dentistry. I am young and have a higher end dental practice incorporating very new technologies and would like my website to reflect that. As many dental patients are older, the website must be very easy to navigate. I would like patients to be able to request appointments, and will eventually add on patient information forms (the health history, etc, that you normally fill out in the practice) from my practice management software, so leave an area for that.

Industry/Entity Type

Building

```html
<!DOCTYPE html>
<html lang="en">
<head>
<meta charset="utf-8">
<title>Colin Marsh, DDS – Our Services</title>
<link href="https://fonts.googleapis.com/css2?family=Open+Sans:wght@400;600;700&display=swap" rel="stylesheet">
<style>
:root{
  --blue:#2a87d8;
  --blue-dark:#1d5fa8;
  --nav-top:#3b95e2;
  --nav-bottom:#1a6fc4;
  --nav-active:#17549a;
  --btn:#134f8f;
  --text:#444;
  --heading:#2f2f2f;
  --cta-bg:#f5f5f5;
  --orange-top:#ff9a2e;
  --orange-bottom:#f97a12;
}
*{margin:0;padding:0;box-sizing:border-box}
html,body{width:1192px;height:1200px;overflow:hidden;background:#fff}
body{font-family:"Open Sans",sans-serif;color:var(--text);position:relative}
.site-header{height:117px;background:linear-gradient(#dcecfb,#fff);position:relative}
.brand{position:absolute;left:107px;top:38px;font-size:34px;font-weight:600;color:var(--blue);letter-spacing:.5px}
.brand-mark{display:inline-block;width:14px;height:14px;border-radius:50%;background:var(--blue);margin-right:10px;vertical-align:middle}
.phone{position:absolute;left:826px;top:36px;display:flex;align-items:center;gap:10px;font-size:28px;color:#3a3a3a}
.main-nav{position:absolute;top:117px;left:0;width:100%;height:44px;background:linear-gradient(var(--nav-top),var(--nav-bottom));display:flex;padding-left:84px}
.main-nav a{color:#fff;text-decoration:none;font-size:15px;line-height:44px;padding:0 30px;border-right:1px solid rgba(255,255,255,.15)}
.main-nav a.home{font-weight:700}
.main-nav a.active{background:var(--nav-active)}
.hero{position:absolute;top:161px;left:0;width:100%;height:253px;background:linear-gradient(90deg,#fff 0%,#e8f2fb 45%,#dbe9f6 100%);border-bottom:1px solid #d6e6f4}
.hero h1{position:absolute;left:110px;top:62px;font-size:58px;font-weight:400;color:var(--blue-dark);letter-spacing:-1px}
.hero h1 strong{font-weight:700}
.hero p{position:absolute;left:111px;top:140px;width:480px;font-size:20px;line-height:27px;color:#333}
.hero-photo{position:absolute;right:0;top:0;width:520px;height:253px;background:linear-gradient(90deg,rgba(220,233,246,0),#c9a98e 35%,#e8c58a 65%,#dfe6ec)}
.section-title{position:absolute;left:112px;top:458px;font-size:24px;color:var(--blue);font-weight:400}
.title-rule{position:absolute;left:260px;top:476px;width:828px;height:3px;border-top:1px dotted #bbb;border-bottom:1px dotted #bbb}
.title-rule::before{content:"";position:absolute;left:0;top:-1px;width:116px;height:3px;background:var(--blue)}
.service{position:absolute;width:500px}
.service .thumb{position:absolute;left:0;top:0;width:149px;height:159px;border:1px solid #ddd}
.service h2{position:absolute;top:-8px;font-size:21px;font-weight:600;color:var(--blue);white-space:nowrap}
.service p{position:absolute;top:30px;font-size:13px;line-height:19px;color:#555}
.service .more{position:absolute;top:144px;background:var(--btn);color:#fff;font-size:13px;padding:7px 10px;text-decoration:none}
.cta{position:absolute;left:110px;top:1023px;width:980px;height:104px;background:var(--cta-bg);border:1px solid #e6e6e6;border-radius:6px}
.cta p{position:absolute;left:18px;top:34px;font-size:26px;color:#555}
.cta a{position:absolute;left:706px;top:23px;width:253px;height:58px;border-radius:3px;background:linear-gradient(var(--orange-top),var(--orange-bottom));color:#fff;text-decoration:none;font-size:19px;display:flex;align-items:center;padding-left:14px;gap:8px}
.site-footer{position:absolute;top:1162px;width:100%;text-align:center;font-size:14px;color:#222}
</style>
</head>
<body>
<header class="site-header">
  <div class="brand"><span class="brand-mark"></span>Colin Marsh, DDS</div>
  <div class="phone">
    <svg width="42" height="42" viewBox="0 0 42 42" aria-hidden="true">
      <circle cx="25" cy="17" r="12" fill="#fff" stroke="#2a87d8" stroke-width="2.5"/>
      <text x="25" y="22" font-size="12" font-weight="700" text-anchor="middle" fill="#2a87d8" font-family="Open Sans,sans-serif">24</text>
      <path d="M6 6c-4 4-3 12 4 20s16 12 21 9l3-3-6-6-4 3c-3-1-8-6-9-9l3-4-6-6z" fill="#2f3a46"/>
    </svg>
    <span>123 555 0199</span>
  </div>
</header>
<nav class="main-nav">
  <a class="home" href="#">HOME</a>
  <a class="active" href="#">SERVICES</a>
  <a href="#">RESOURCES</a>
  <a href="#">PORTFOLIO</a>
  <a href="#">TEAM</a>
  <a href="#">CONTACT</a>
</nav>
<section class="hero">
  <h1>Our <strong>Services</strong></h1>
  <p>Lorem Ipsum is simply dummy text of the printing and typesetting industry. Lorem Ipsum has been</p>
  <div class="hero-photo" role="img" aria-label="Photo of a smiling family of three"></div>
</section>
<h2 class="section-title">Our Services</h2>
<div class="title-rule"></div>

<article class="service" style="left:109px;top:547px">
  <div class="thumb" role="img" aria-label="Photo of a smiling woman" style="background:linear-gradient(135deg,#f3d9c6,#e9b99c 60%,#fff)"></div>
  <h2 style="left:163px">Cosmetics</h2>
  <p style="left:167px;width:345px">we believe that "prevention is better than cure". That's why we offer an one hour comprehensive oral examina-tion, which includes a virtual tour of your mouth, intra-oral photos, scale and clean, polish, fluoride treatment and X-rays as required, to ensure you are receiving the</p>
  <a class="more" href="#" style="left:167px">Read More</a>
</article>

<article class="service" style="left:659px;top:547px">
  <div class="thumb" role="img" aria-label="Illustration of a dental implant in the gum" style="background:linear-gradient(160deg,#fff,#eef1f4 45%,#e79cb0)"></div>
  <h2 style="left:168px">Preventive care</h2>
  <p style="left:169px;width:260px">we believe that "prevention is better than cure". That's why we offer an one hour comprehensive oral examination, which includes a virtual tour of your mouth, intra-oral photos, scale and clean, polish,</p>
  <a class="more" href="#" style="left:178px">Read More</a>
</article>

<article class="service" style="left:109px;top:801px">
  <div class="thumb" role="img" aria-label="Illustration of a dental bridge over implants" style="background:linear-gradient(#fff,#f0eded 45%,#d98a8f)"></div>
  <h2 style="left:166px;font-size:25px;top:-12px">Restorative Procedures</h2>
  <p style="left:167px;width:345px">we believe that "prevention is better than cure". That's why we offer an one hour comprehensive oral examina-tion, which includes a virtual tour of your mouth, intra-oral photos, scale and clean, polish, fluoride treatment and X-rays as required, to ensure you are receiving the</p>
  <a class="more" href="#" style="left:167px">Read More</a>
</article>

<article class="service" style="left:659px;top:801px">
  <div class="thumb" role="img" aria-label="Photo of a smiling woman biting a green apple" style="background:linear-gradient(135deg,#6b4a36,#d7a98c 50%,#9bc24a)"></div>
  <h2 style="left:168px">Dental implants</h2>
  <p style="left:169px;width:260px">we believe that "prevention is better than cure". That's why we offer an one hour comprehensive oral examination, which includes a virtual tour of your mouth, intra-oral photos, scale and clean, polish,</p>
  <a class="more" href="#" style="left:187px">Read More</a>
</article>

<section class="cta">
  <p>Want to Get Treated? Schedule Your Appointment Now!</p>
  <a href="#">Request Appointment
    <svg width="28" height="26" viewBox="0 0 28 26" aria-hidden="true" fill="none" stroke="#5a3a10" stroke-width="1.6">
      <rect x="2" y="4" width="24" height="20" rx="2"/>
      <line x1="8" y1="1" x2="8" y2="7"/><line x1="20" y1="1" x2="20" y2="7"/>
      <g fill="#5a3a10" stroke="none"><rect x="7" y="11" width="3" height="3"/><rect x="12.5" y="11" width="3" height="3"/><rect x="18" y="11" width="3" height="3"/><rect x="7" y="17" width="3" height="3"/><rect x="12.5" y="17" width="3" height="3"/><rect x="18" y="17" width="3" height="3"/></g>
    </svg>
  </a>
</section>
<footer class="site-footer">© Copyrights 2014 All rights Reserved</footer>
</body>
</html>
```